Outstanding Gift box (Kraft Mailer box) design needed

We are in need of an outstanding gift box design for our new product line. This design will include inside and outside of box. We are looking for a modern design and have included samples, die line and text for the box. We need a designer that can take this information and create something amazing!

Colors

Designer to choose colors to be used in the design.

Requirements
Must have
• Modern design, logo, please see sample boxes attached. Logo color can be change to compliment color on outer box.
• We love the colors in the sample images
• Google link to bamboo stalk/leaves: https://files.plorvexa.net/view?ref=7QK2TzR9mWxLb4HsN0pVdYe3CuAj8GfKo
• Please provide mock up of your design on a Kraft mailer box (brown box)
Nice to have
• light bamboo silhouette on the inside of the box and maybe a modern bamboo silhouette (can be color) on the outside of box

```html
<!DOCTYPE html>
<html lang="en">
<head>
<meta charset="utf-8">
<title>Vela Home – Air Purifying Bags mailer box dieline</title>
<link href="https://fonts.googleapis.com/css2?family=Oswald:wght@600&family=Montserrat:wght@400;500;600&display=swap" rel="stylesheet">
<style>
  :root{
    --page:#ececec;
    --kraft:#caa473;
    --kraft-edge:#7d6446;
    --navy:#154463;
    --ink:#1f2a33;
    --bamboo-dark:#3b3226;
  }
  html,body{margin:0;padding:0;width:811px;height:1200px;overflow:hidden;background:var(--page);}
  .dieline{position:absolute;left:10px;top:209px;width:790px;height:781px;}
  .panel{fill:var(--kraft);stroke:var(--kraft-edge);stroke-width:.8;}
  .fold{stroke:var(--kraft-edge);stroke-width:.7;stroke-dasharray:3 3;fill:none;}
  .band{fill:var(--navy);}
  .headline{font-family:"Oswald",sans-serif;font-weight:600;fill:var(--kraft);text-anchor:middle;}
  .body-text{font-family:"Montserrat",sans-serif;fill:var(--ink);}
  .band-copy{font-family:"Montserrat",sans-serif;fill:var(--kraft);text-anchor:middle;font-size:11px;}
  .brand-name{font-family:"Montserrat",sans-serif;font-weight:500;fill:var(--ink);letter-spacing:1px;}
  .brand-square{fill:var(--navy);}
  .brand-frame{fill:none;stroke:var(--ink);stroke-width:1.5;}
  .icon-ring{fill:none;stroke:var(--navy);stroke-width:1.4;}
  .pill-text{font-family:"Montserrat",sans-serif;font-weight:500;fill:#fff;font-size:9px;text-anchor:middle;}
  .warning-box{fill:none;stroke:var(--ink);stroke-width:.8;}
  .support-title{fill:var(--navy);}
</style>
</head>
<body>
<svg class="dieline" viewBox="50 550 905 895" xmlns="http://www.w3.org/2000/svg">
  <defs>
    <linearGradient id="bambooTone" x1="0" y1="0" x2="1" y2="1">
      <stop offset="0" stop-color="#3b3226" stop-opacity=".45"/>
      <stop offset=".5" stop-color="#3b3226" stop-opacity=".2"/>
      <stop offset="1" stop-color="#3b3226" stop-opacity=".4"/>
    </linearGradient>
    <clipPath id="lidShape">
      <rect x="185" y="1055" width="640" height="270" rx="22"/>
      <rect x="180" y="1325" width="648" height="115" rx="22"/>
    </clipPath>
  </defs>

  <!-- panels -->
  <rect class="panel" x="133" y="555" width="742" height="113"/>
  <rect class="panel" x="60" y="668" width="115" height="272"/>
  <rect class="panel" x="175" y="668" width="655" height="272"/>
  <rect class="panel" x="830" y="668" width="118" height="272"/>
  <rect class="panel" x="133" y="940" width="742" height="115"/>
  <rect class="panel" x="185" y="1055" width="640" height="270" rx="22"/>
  <rect class="panel" x="180" y="1325" width="648" height="115" rx="22"/>

  <!-- bamboo artwork areas -->
  <rect x="675" y="555" width="155" height="385" fill="url(#bambooTone)" role="img" aria-label="Ink-brush bamboo stalks and leaves illustration"/>
  <rect x="180" y="1055" width="155" height="385" fill="url(#bambooTone)" clip-path="url(#lidShape)" role="img" aria-label="Ink-brush bamboo stalks and leaves illustration"/>

  <!-- folds -->
  <path class="fold" d="M293 555V1055M715 555V1055M133 668H875M133 940H875M185 1055H825M185 1325H825"/>

  <!-- colour band -->
  <rect class="band" x="555" y="555" width="120" height="885"/>
  <line x1="570" y1="1222" x2="662" y2="1222" stroke="var(--kraft)" stroke-width=".8"/>

  <!-- top wall (upside down) -->
  <g transform="rotate(180 615 612)">
    <text class="headline" x="615" y="592" font-size="30">AIR</text>
    <text class="headline" x="615" y="622" font-size="30" textLength="112" lengthAdjust="spacingAndGlyphs">PURIFYING</text>
    <text class="headline" x="615" y="652" font-size="30">BAGS</text>
  </g>
  <g transform="rotate(180 434 611)">
    <rect class="brand-frame" x="405" y="582" width="58" height="58"/>
    <rect class="brand-square" x="413" y="590" width="42" height="42"/>
    <text class="brand-name" font-size="8" transform="translate(472 584) rotate(90)">VELA HOME</text>
  </g>

  <!-- front wall (upside down) -->
  <g transform="rotate(180 615 998)">
    <text class="headline" x="615" y="978" font-size="30">AIR</text>
    <text class="headline" x="615" y="1008" font-size="30" textLength="112" lengthAdjust="spacingAndGlyphs">PURIFYING</text>
    <text class="headline" x="615" y="1038" font-size="30">BAGS</text>
  </g>
  <g transform="rotate(180 434 997)">
    <rect class="brand-frame" x="405" y="968" width="58" height="58"/>
    <rect class="brand-square" x="413" y="976" width="42" height="42"/>
    <text class="brand-name" font-size="8" transform="translate(472 970) rotate(90)">VELA HOME</text>
  </g>

  <!-- box floor -->
  <rect x="557" y="745" width="116" height="115" fill="none" stroke="var(--kraft)" stroke-width="1.5"/>
  <rect class="brand-square" x="570" y="757" width="90" height="92" stroke="var(--kraft)" stroke-width=".8"/>
  <text class="brand-name" font-size="14" transform="translate(550 862) rotate(-90)">VELA HOME</text>

  <g transform="rotate(180 415 800)">
    <text class="body-text support-title" x="415" y="714" font-size="11" text-anchor="middle">For support contact</text>
    <text class="body-text" x="415" y="740" font-size="9" text-anchor="middle">care@velahomegoods.example</text>
    <text class="body-text" x="415" y="753" font-size="9" text-anchor="middle">or visit us at: www.velahomegoods.example</text>
    <rect class="warning-box" x="352" y="767" width="126" height="62" rx="5"/>
    <text class="body-text" x="415" y="781" font-size="7" font-weight="600" text-anchor="middle">⚠ WARNING</text>
    <text class="body-text" x="415" y="792" font-size="5.5" text-anchor="middle">To avoid danger of suffocation, keep</text>
    <text class="body-text" x="415" y="800" font-size="5.5" text-anchor="middle">this plastic bag away from babies and</text>
    <text class="body-text" x="415" y="808" font-size="5.5" text-anchor="middle">children. Do not use this bag in cribs,</text>
    <text class="body-text" x="415" y="816" font-size="5.5" text-anchor="middle">beds, carriages or play pens.</text>
    <text class="body-text" x="415" y="824" font-size="5.5" font-weight="600" text-anchor="middle">This bag is not a toy.</text>
    <circle cx="415" cy="856" r="7" fill="none" stroke="var(--navy)" stroke-width="2.5" stroke-dasharray="8 3"/>
    <text class="body-text" x="415" y="880" font-size="7" text-anchor="middle">Made in China</text>
  </g>

  <!-- side flaps -->
  <text class="brand-name" x="205" y="772" font-size="9">VELA HOME</text>
  <rect class="brand-frame" x="205" y="776" width="62" height="60"/>
  <rect class="brand-square" x="213" y="784" width="46" height="44"/>
  <g transform="rotate(90 770 790)">
    <rect class="brand-frame" x="740" y="760" width="60" height="60"/>
    <rect class="brand-square" x="748" y="768" width="44" height="44"/>
  </g>
  <text class="brand-name" font-size="8" transform="translate(738 826) rotate(180)" text-anchor="end">VELA HOME</text>

  <!-- lid -->
  <text class="brand-name" x="362" y="1090" font-size="14">HOME COLLECTION</text>
  <rect class="brand-frame" x="362" y="1110" width="116" height="118"/>
  <rect class="brand-square" x="373" y="1123" width="94" height="94"/>
  <text class="brand-name" font-size="15" transform="translate(486 1112) rotate(90)">VELA HOME</text>

  <circle class="icon-ring" cx="361" cy="1260" r="13"/>
  <circle cx="361" cy="1260" r="7" fill="none" stroke="var(--navy)" stroke-width="1.2"/>
  <path d="M354 1260H368M361 1253V1267" stroke="var(--navy)" stroke-width="1"/>
  <circle class="icon-ring" cx="421" cy="1260" r="13"/>
  <path d="M416 1253V1267M425 1253C428 1256 428 1261 425 1263V1267" stroke="var(--navy)" stroke-width="1.2" fill="none"/>
  <circle class="icon-ring" cx="481" cy="1260" r="13"/>
  <rect x="476" y="1256" width="10" height="11" rx="2" fill="none" stroke="var(--navy)" stroke-width="1.2"/>
  <rect x="479" y="1251" width="4" height="5" fill="none" stroke="var(--navy)" stroke-width="1.2"/>

  <text class="body-text" x="332" y="1287" font-size="8">Earth Friendly  |  Non - Toxic  |  Fragrance Free</text>

  <path class="band" d="M350 1303H503L497 1324H345Z"/>
  <text class="pill-text" x="424" y="1317">REUSABLE FOR UP TO 2 YEARS</text>

  <text class="headline" x="615" y="1118" font-size="44">AIR</text>
  <text class="headline" x="615" y="1160" font-size="44" textLength="114" lengthAdjust="spacingAndGlyphs">PURIFYING</text>
  <text class="headline" x="615" y="1202" font-size="44">BAGS</text>
  <text class="band-copy" x="615" y="1248">Activated</text>
  <text class="band-copy" x="615" y="1261">bamboo</text>
  <text class="band-copy" x="615" y="1274">charcoal plus</text>
  <text class="band-copy" x="615" y="1287">clay moisture</text>
  <text class="band-copy" x="615" y="1300">absorbing beads</text>

  <!-- lid front -->
  <text class="body-text" x="335" y="1385" font-size="13" font-weight="500">[PU(RE) + (FR)ESH] = AIR</text>
  <text class="headline" x="615" y="1362" font-size="33">AIR</text>
  <text class="headline" x="615" y="1396" font-size="33" textLength="114" lengthAdjust="spacingAndGlyphs">PURIFYING</text>
  <text class="headline" x="615" y="1430" font-size="33">BAGS</text>
</svg>
</body>
</html>
```